Business Card - Existing Logo & Branding copied to Business Card Format

We are looking for a designer to help with designing a two sided business card for us. We sell a web based software platform that helps people sell access to online training.
We have an existing logo and recently completed a design project here on draft hive to have someone design a nice trade show booth for us (also attached file for that design as well as our logo). We really like the look and feel of the tradeshow booth design. The fonts, colors, etc all work for us. We are hoping someone can create something very similar just in business card format.
Should be pretty straight forward hopefully....
On one side we want the logo, employee name, email address, phone and fax. On the other side we would like the text "transform your organizations training, revenue products = revenue" - See the attached PSD for what we want that to look like.
You can also see our website at www.tutorvane.com for an example of our branding.
We are open to ideas, have done several projects on draft hive and love when designers come up with creative approaches that are even better then what we envisioned.
Software

```html
<!DOCTYPE html>
<html lang="en">
<head>
<meta charset="utf-8">
<title>TutorVane Business Card</title>
<link rel="stylesheet" href="https://fonts.googleapis.com/css2?family=Arvo:wght@700&family=Fira+Sans:wght@500;600&family=Michroma&family=Montserrat:wght@500&display=swap">
<style>
  :root {
    --brand-red: #b01e24;
    --accent-red: #c9534a;
    --ink-dark: #3a3a3c;
    --ink-grey: #5f5f5f;
    --paper: #ffffff;
    --stage-dark: #060708;
    --bulb-tone: #d9d9d9;
    --photo-tone: #8a7f76;
  }
  * { margin: 0; padding: 0; box-sizing: border-box; }
  html, body { width: 1200px; height: 1000px; overflow: hidden; background: var(--paper); }
  .board { position: relative; width: 1200px; height: 1000px; }

  .card {
    position: absolute; width: 398px; height: 228px;
    background: var(--paper);
    box-shadow: 6px 8px 10px rgba(0,0,0,.55);
    overflow: hidden;
  }
  .card--back { width: 395px; height: 225px; }
  .card--mini { transform-origin: 0 0; transform: scale(.605); }
  .card--mini.card--front { z-index: 3; }
  .card--mini.card--back { z-index: 2; }

  .brand-square { position: absolute; left: 29px; top: 31px; width: 62px; height: 62px; background: var(--brand-red); }
  .brand-name {
    position: absolute; left: 109px; top: 34px;
    font: 600 44px/1 "Fira Sans", sans-serif; letter-spacing: -1px; color: var(--ink-dark);
  }
  .contact {
    position: absolute; right: 16px; top: 132px; text-align: right;
    font: 600 10.5px/17px "Fira Sans", sans-serif; letter-spacing: 1px; color: var(--ink-dark);
  }
  .contact .value { color: var(--brand-red); }

  .tagline-intro { position: absolute; left: 45px; top: 42px; font: 500 12px/1 "Montserrat", sans-serif; color: #444; }
  .tagline-focus {
    position: absolute; left: 86px; top: 61px;
    font: 700 12.5px/15px "Arvo", serif; letter-spacing: 1px; color: var(--accent-red);
  }
  .tagline-focus .joiner { color: var(--ink-dark); }
  .revenue { position: absolute; left: 241px; top: 162px; font: 700 19px/1 "Arvo", serif; letter-spacing: .5px; color: var(--ink-grey); }
  .bulb { position: absolute; left: 140px; top: 113px; width: 32px; height: 52px; border-radius: 16px 16px 6px 6px; background: linear-gradient(#eee, var(--bulb-tone)); }
  .money-photo { position: absolute; left: 291px; top: 99px; width: 58px; height: 53px; background: linear-gradient(135deg, #cfcac4, var(--photo-tone) 60%, #4a423c); }
  .equation { position: absolute; left: 0; top: 0; }

  .caption { position: absolute; font: 13px/1 "Michroma", sans-serif; letter-spacing: 2px; color: #111; font-variant: small-caps; }
  .stage { position: absolute; left: 0; top: 716px; width: 1200px; height: 284px; background: var(--stage-dark); z-index: 1; }
</style>
</head>
<body>
<main class="board">

  <section class="card card--front" style="left:137px; top:146px;">
    <div class="brand-square"></div>
    <div class="brand-name">TutorVane</div>
    <div class="contact">
      <p class="value">Ned Parlow</p>
      <p class="value">nparlow@postlark.com</p>
      <p>Phone: <span class="value">555.555.5555</span></p>
      <p>Fax: <span class="value">555.555.4444</span></p>
    </div>
  </section>
  <p class="caption" style="left:311px; top:416px;">Front</p>

  <section class="card card--back" style="left:650px; top:308px;">
    <p class="tagline-intro">Transform your organization's</p>
    <p class="tagline-focus">TRAINING, INFORMATION<br><span class="joiner">and</span> PRODUCTS</p>
    <svg class="equation" width="395" height="225" viewBox="0 0 395 225">
      <g stroke="var(--brand-red)" stroke-width="1.6" fill="none">
        <line x1="193" y1="97" x2="207" y2="110"/>
        <line x1="179" y1="126" x2="202" y2="125"/>
        <line x1="238" y1="126" x2="280" y2="127"/>
        <line x1="222" y1="140" x2="238" y2="153"/>
      </g>
      <g stroke="var(--ink-grey)" stroke-width="2.4">
        <line x1="212" y1="122" x2="228" y2="122"/>
        <line x1="212" y1="128" x2="228" y2="128"/>
      </g>
    </svg>
    <div class="bulb" role="img" aria-label="Sketch of a light bulb"></div>
    <div class="money-photo" role="img" aria-label="Photo of a hand holding banknotes"></div>
    <p class="revenue">Revenue</p>
  </section>
  <p class="caption" style="left:836px; top:578px;">Back</p>

  <div class="stage"></div>

  <section class="card card--back card--mini" style="left:920px; top:828px;">
    <p class="tagline-intro">Transform your organization's</p>
    <p class="tagline-focus">TRAINING, INFORMATION<br><span class="joiner">and</span> PRODUCTS</p>
    <svg class="equation" width="395" height="225" viewBox="0 0 395 225">
      <g stroke="var(--brand-red)" stroke-width="1.6" fill="none">
        <line x1="193" y1="97" x2="207" y2="110"/>
        <line x1="179" y1="126" x2="202" y2="125"/>
        <line x1="238" y1="126" x2="280" y2="127"/>
        <line x1="222" y1="140" x2="238" y2="153"/>
      </g>
      <g stroke="var(--ink-grey)" stroke-width="2.4">
        <line x1="212" y1="122" x2="228" y2="122"/>
        <line x1="212" y1="128" x2="228" y2="128"/>
      </g>
    </svg>
    <div class="bulb" role="img" aria-label="Sketch of a light bulb"></div>
    <div class="money-photo" role="img" aria-label="Photo of a hand holding banknotes"></div>
    <p class="revenue">Revenue</p>
  </section>

  <section class="card card--front card--mini" style="left:737px; top:748px;">
    <div class="brand-square"></div>
    <div class="brand-name">TutorVane</div>
    <div class="contact">
      <p class="value">Ned Parlow</p>
      <p class="value">nparlow@postlark.com</p>
      <p>Phone: <span class="value">555.555.5555</span></p>
      <p>Fax: <span class="value">555.555.4444</span></p>
    </div>
  </section>

</main>
</body>
</html>
```